BrightMop Tidewater Commercial Cleaning Brochure

We need a tri fold brochure that we can use to market our commercial cleaning services to clients. We are looking for something that will stand out. We don't want to use any faces of people on the brochures, only cleaning tools and supplies. We offer Office Cleaning, Covid Cleaning, Janitorial and Floor Services

Target Market(s)

Small to large businesses

Industry/Entity Type

Commercial Cleaning

Colors
0054AA
0677BA
7BADD7
CADEEF
E8F1F8
0094D4
00A9DD
6FCCEA
C7EBF8
E9F6FB
00AB8E
00BBA5
67D7C9
C6EFE9
E9F9F6
59FF00
82FF00
B8FF75
E3FFCB
F4FFEA

Requirements
Must have
• Stand out design-Eye Catching
Should not have
• faces of ppl the brochure

```html
<!DOCTYPE html>
<html lang="en">
<head>
<meta charset="UTF-8">
<title>BrightMop Tidewater – Commercial Cleaning Brochure</title>
<link href="https://fonts.googleapis.com/css2?family=Montserrat:wght@400;500;600;700;800;900&display=swap" rel="stylesheet">
<style>
  :root{
    --blue:#0658a4;
    --blue-deep:#0054AA;
    --sky:#0094D4;
    --green:#8cc63f;
    --green-light:#9fd04a;
    --paper:#f7f8f9;
    --paper-shade:#eef0f2;
    --ink:#222831;
    --white:#ffffff;
    --stage:#5e5e5e;
  }
  *{box-sizing:border-box;margin:0;padding:0}
  html,body{width:831px;height:1200px;overflow:hidden}
  body{background:var(--stage);font-family:'Montserrat',sans-serif;color:var(--ink);position:relative}

  .sheet{position:absolute;left:89px;width:653px;height:462px;background:var(--paper);overflow:hidden;box-shadow:0 10px 18px rgba(0,0,0,.35)}
  .sheet--outside{top:105px}
  .sheet--inside{top:635px}
  .fold{position:absolute;top:0;bottom:0;width:1px;background:rgba(0,0,0,.06)}
  .backdrop{position:absolute;left:0;top:0}
  .abs{position:absolute}

  .photo{position:absolute;border-radius:50%;}
  .photo--blue{border:4px solid var(--blue);box-shadow:0 0 0 2px var(--white)}
  .photo--green{border:5px solid var(--green);box-shadow:0 0 0 2px var(--white)}

  /* Outside */
  .offer-title{left:22px;top:25px;width:173px;height:33px;background:var(--blue);color:var(--white);font-weight:900;font-size:25px;line-height:33px;text-align:center;letter-spacing:.3px}
  .offer-title span{color:var(--green)}
  .offer-list{left:25px;top:68px;list-style:none}
  .offer-list li{display:flex;align-items:center;gap:4px;font-weight:800;font-size:12.3px;line-height:16.8px;color:#1f2a36;letter-spacing:.2px}
  .offer-list svg{width:10px;height:10px;flex:none}

  .section-tab{background:var(--blue);color:var(--white);font-weight:800;text-align:center}
  .testimonials-title{left:238px;top:26px;width:176px;height:24px;font-size:14px;line-height:24px;border-radius:0 3px 3px 0}
  .quote{position:absolute;left:240px;width:172px;border:1px solid var(--sky);border-radius:6px;padding:11px 6px 7px 11px;font-size:5.9px;line-height:8.4px;color:#222}
  .quote::before{content:"\201C";position:absolute;left:9px;top:-7px;height:13px;font-size:24px;line-height:22px;font-weight:800;color:var(--sky);background:var(--paper);padding:0 2px;overflow:hidden}
  .quote cite{display:block;text-align:right;font-style:normal;font-weight:700;margin-top:4px;padding-right:24px}
  .quote::after{content:"\201D";position:absolute;right:5px;bottom:-8px;height:15px;font-size:24px;line-height:22px;font-weight:800;color:var(--sky);background:var(--paper);padding:0 2px;overflow:hidden}
  .quote--one{top:72px}
  .quote--two{top:145px}

  .brand{display:flex;align-items:center;color:var(--blue);font-weight:600;white-space:nowrap}
  .brand i{display:block;border-radius:50%;background:var(--green)}
  .brand--small{left:258px;top:222px;width:140px;font-size:14px;line-height:16px;flex-direction:column}
  .brand--small i{width:8px;height:8px;position:absolute;right:12px;top:3px}
  .brand--large{left:462px;top:30px;width:162px;font-size:20px;line-height:22px;flex-direction:column;gap:2px}
  .brand--large i{width:11px;height:11px;position:absolute;right:8px;top:5px}

  .about-title,.contact-title{font-size:16px;font-weight:400;color:var(--white);letter-spacing:.3px;padding-bottom:2px;border-bottom:1px solid var(--white)}
  .about-title b,.contact-title b{font-weight:800}
  .about-title{left:33px;top:340px;width:151px}
  .contact-title{left:251px;top:340px;width:151px}
  .about-copy{left:33px;top:375px;width:155px;font-size:7.6px;line-height:9.5px;color:var(--white);font-weight:500}
  .contact-list{left:251px;top:375px;list-style:none;color:var(--white);font-size:9.4px;font-weight:500}
  .contact-list li{display:flex;gap:5px;align-items:flex-start;line-height:11px;margin-bottom:5.5px}
  .contact-list svg{width:7px;height:7px;margin-top:2px;flex:none}

  .headline{left:461px;top:305px;width:165px;text-align:center;font-weight:900;color:var(--white);font-size:20.5px;line-height:24px}
  .headline-box{position:absolute;left:468px;width:155px;height:26px;text-align:center;font-weight:900;font-size:21px;line-height:26px}
  .headline-box--blue{top:332px;background:var(--blue);color:var(--white)}
  .headline-box--white{top:358px;background:var(--white);color:var(--blue);border:1px solid var(--blue)}
  .phone-pill{left:461px;top:404px;width:165px;height:23px;border:1.5px solid var(--white);border-radius:12px;background:var(--blue);color:var(--white);font-weight:800;font-size:16px;display:flex;align-items:center;justify-content:center;gap:5px}
  .phone-pill svg{width:12px;height:12px}
  .web-line{left:440px;width:210px;text-align:center;color:var(--white);font-weight:700;font-size:10.6px}
  .web-line--outside{top:431px}

  /* Inside */
  .service-tab{position:absolute;height:25px;width:176px;font-size:11.6px;line-height:25px;border-radius:0 3px 3px 0;text-align:left;padding-left:18px;letter-spacing:.2px}
  .service-tab--office{left:21px;top:25px}
  .service-tab--covid{left:238px;top:25px;padding-left:22px}
  .service-tab--floor{left:456px;top:25px;padding-left:23px}
  .service-tab--janitorial{left:238px;top:151px;padding-left:22px}
  .service-copy{position:absolute;width:178px;font-size:7.2px;line-height:9.5px;color:#1e242b}
  .service-copy p+p{margin-top:9.5px}
  .service-copy--office{left:21px;top:62px}
  .service-copy--covid{left:238px;top:62px}
  .service-copy--floor{left:456px;top:62px}
  .service-copy--janitorial{left:238px;top:185px}

  .call-now{left:460px;top:353px;width:170px;text-align:center;color:var(--white);font-weight:800;font-size:14.5px}
  .estimate{left:459px;top:375px;width:171px;height:24px;background:var(--green);color:var(--white);font-weight:900;font-size:16.5px;line-height:24px;text-align:center}
  .phone-big{left:460px;top:405px;width:170px;display:flex;justify-content:center;align-items:center;gap:5px;color:var(--white);font-weight:800;font-size:17px}
  .phone-big svg{width:13px;height:13px}
  .web-line--inside{top:430px}
</style>
</head>
<body>

<section class="sheet sheet--outside">
  <svg class="backdrop" width="653" height="462" viewBox="0 0 653 462" aria-hidden="true">
    <path d="M0,282 C110,345 230,352 320,335 C430,314 520,280 653,292 L653,462 L0,462 Z" fill="var(--green)"/>
    <path d="M60,285 C150,330 240,338 320,322 C430,300 520,262 653,272" fill="none" stroke="var(--blue)" stroke-width="15"/>
  </svg>
  <div class="fold" style="left:217px"></div>
  <div class="fold" style="left:435px"></div>

  <h2 class="abs offer-title">WE <span>OFFER</span></h2>
  <ul class="abs offer-list">
    <li><svg viewBox="0 0 10 10"><circle cx="5" cy="5" r="4.3" fill="none" stroke="var(--blue)" stroke-width="1"/><path d="M3,5.1 L4.5,6.5 L7,3.8" fill="none" stroke="var(--blue)" stroke-width="1"/></svg>OFFICE CLEANING</li>
    <li><svg viewBox="0 0 10 10"><circle cx="5" cy="5" r="4.3" fill="none" stroke="var(--blue)" stroke-width="1"/><path d="M3,5.1 L4.5,6.5 L7,3.8" fill="none" stroke="var(--blue)" stroke-width="1"/></svg>COVID CLEANING</li>
    <li><svg viewBox="0 0 10 10"><circle cx="5" cy="5" r="4.3" fill="none" stroke="var(--blue)" stroke-width="1"/><path d="M3,5.1 L4.5,6.5 L7,3.8" fill="none" stroke="var(--blue)" stroke-width="1"/></svg>JANITORIAL</li>
    <li><svg viewBox="0 0 10 10"><circle cx="5" cy="5" r="4.3" fill="none" stroke="var(--blue)" stroke-width="1"/><path d="M3,5.1 L4.5,6.5 L7,3.8" fill="none" stroke="var(--blue)" stroke-width="1"/></svg>FLOOR SERVICES</li>
  </ul>

  <div class="photo photo--blue" role="img" aria-label="Protective-suited worker wiping a row of waiting room chairs" style="left:101px;top:154px;width:150px;height:150px;background:radial-gradient(circle at 45% 40%,#f1f3f5,#c4c9cf 60%,#55595e)"></div>
  <div class="photo photo--blue" role="img" aria-label="Gloved hand spraying and wiping a white surface" style="left:46px;top:144px;width:86px;height:86px;background:radial-gradient(circle at 50% 60%,#eef2f6,#c9d4e0 60%,#8da6c4)"></div>

  <h2 class="abs section-tab testimonials-title">TESTIMONIALS</h2>
  <blockquote class="quote quote--one">Lorem ipsum dolor sit amet, consectetur adipiscing elit, sed do eiusmod tempor incididunt ut labore et dolore magna aliqua. Ut enim ad minim veniam.<cite>-Lorem ipsum</cite></blockquote>
  <blockquote class="quote quote--two">Duis aute irure dolor in reprehenderit in voluptate velit esse cillum dolore eu fugiat nulla pariatur. Excepteur sint occaecat cupidatat non proident, sunt in culpa qui officia deserunt mollit anim id.<cite>Lorem ipsum dolor</cite></blockquote>

  <div class="abs brand brand--small"><span>BrightMop</span><span>Tidewater</span><i></i></div>

  <div class="abs brand brand--large"><span>BrightMop</span><span>Tidewater</span><i></i></div>

  <div class="photo photo--blue" role="img" aria-label="Mopping a hallway floor beside a yellow wet floor caution sign" style="left:407px;top:98px;width:182px;height:182px;background:radial-gradient(circle at 55% 55%,#f4c531 0,#e9e6df 30%,#d7d3cc 65%,#9aa6a0)"></div>
  <div class="photo photo--blue" role="img" aria-label="Janitorial cart loaded with buckets, mops and supplies" style="left:556px;top:147px;width:98px;height:98px;background:radial-gradient(circle at 50% 60%,#f0c52a 0,#6a7075 45%,#3a3f44)"></div>

  <h2 class="abs about-title">ABOUT <b>US</b></h2>
  <p class="abs about-copy">BrightMop Tidewater is commercial cleaning company that specializes in the cleaning of Hospitals, Surgery Centers, Outpatient Facilities, Medical Office Buildings, Dental Offices, Emergency Clinics, and more. We customize our services to meet your specific needs</p>

  <h2 class="abs contact-title">CONTACT <b>US</b></h2>
  <ul class="abs contact-list">
    <li><svg viewBox="0 0 8 8"><path d="M4,0.5 C2.4,0.5 1.3,1.6 1.3,3 C1.3,4.8 4,7.5 4,7.5 C4,7.5 6.7,4.8 6.7,3 C6.7,1.6 5.6,0.5 4,0.5 Z" fill="none" stroke="#fff" stroke-width=".8"/><circle cx="4" cy="3" r="1" fill="#fff"/></svg><span>2207 Harbor Point Ave,<br>Norfolk, VA 23510, USA</span></li>
    <li><svg viewBox="0 0 8 8"><rect x=".5" y="1.5" width="7" height="5" fill="none" stroke="#fff" stroke-width=".8"/><path d="M.5,1.5 L4,4.5 L7.5,1.5" fill="none" stroke="#fff" stroke-width=".8"/></svg>hello@brightmoptidewater.com</li>
    <li><svg viewBox="0 0 8 8"><circle cx="4" cy="4" r="3.5" fill="none" stroke="#fff" stroke-width=".8"/><path d="M2.7,2.2 L3.5,3.3 L3.2,3.8 C3.6,4.5 3.9,4.8 4.3,5 L4.8,4.6 L5.8,5.4 L5.2,6 C3.8,5.8 2.4,4.3 2.2,2.8 Z" fill="#fff"/></svg>757-555-0142</li>
    <li><svg viewBox="0 0 8 8"><circle cx="4" cy="4" r="3.5" fill="none" stroke="#fff" stroke-width=".8"/><ellipse cx="4" cy="4" rx="1.5" ry="3.5" fill="none" stroke="#fff" stroke-width=".6"/><path d="M.5,4 H7.5" stroke="#fff" stroke-width=".6"/></svg>www.brightmoptidewater.com</li>
  </ul>

  <h1 class="abs headline">COMMERCIAL</h1>
  <div class="headline-box headline-box--blue">CLEANING</div>
  <div class="headline-box headline-box--white">SERVICES</div>
  <div class="abs phone-pill"><svg viewBox="0 0 12 12"><circle cx="6" cy="6" r="5.2" fill="none" stroke="#fff" stroke-width="1"/><path d="M4,3.2 L5.2,4.8 L4.8,5.6 C5.3,6.6 5.8,7 6.4,7.3 L7.1,6.8 L8.6,8 L7.8,8.8 C5.7,8.5 3.6,6.3 3.3,4.1 Z" fill="#fff"/></svg>757-555-0142</div>
  <p class="abs web-line web-line--outside">www.brightmoptidewater.com</p>
</section>

<section class="sheet sheet--inside">
  <svg class="backdrop" width="653" height="462" viewBox="0 0 653 462" aria-hidden="true">
    <path d="M0,205 C60,330 200,420 360,390 C470,368 570,295 653,195 L653,462 L0,462 Z" fill="var(--blue)"/>
    <path d="M300,392 C420,385 560,290 653,200" fill="none" stroke="var(--green)" stroke-width="16"/>
  </svg>
  <div class="fold" style="left:217px"></div>
  <div class="fold" style="left:435px"></div>

  <h2 class="section-tab service-tab service-tab--office">OFFICE CLEANING</h2>
  <div class="service-copy service-copy--office">
    <p>Lorem ipsum dolor sit amet, consectetur adipiscing elit, sed do eiusmod tempor incididunt ut labore et dolore magna aliqua. Ut enim ad minim veniam, quis nostrud exercitation ullamco laboris nisi ut aliquip ex ea commodo consequat. Duis aute irure dolor in reprehenderit in voluptate velit esse cillum dolore eu fugiat nulla pariatur.</p>
    <p>Excepteur sint occaecat cupidatat non proident, sunt in culpa qui officia deserunt mollit anim id est laborum.</p>
  </div>

  <h2 class="section-tab service-tab service-tab--covid">COVID CLEANING</h2>
  <div class="service-copy service-copy--covid">
    <p>Lorem ipsum dolor sit amet, consectetur adipiscing elit, sed do eiusmod tempor incididunt ut labore et dolore magna aliqua. Ut enim ad minim veniam, quis nostrud exercitation ullamco laboris nisi ut aliquip ex ea commodo consequat. Duis aute irure dolor in reprehenderit in voluptate velit esse cillum dolore eu fugiat nulla pariatur.</p>
  </div>

  <h2 class="section-tab service-tab service-tab--janitorial">JANITORIAL</h2>
  <div class="service-copy service-copy--janitorial">
    <p>Lorem ipsum dolor sit amet, consectetur adipiscing elit, sed do eiusmod tempor incididunt ut labore et dolore magna aliqua. Ut enim ad minim veniam, quis nostrud exercitation ullamco laboris nisi ut aliquip ex ea commodo consequat. Duis aute irure dolor in reprehenderit in voluptate velit esse cillum dolore eu fugiat nulla pariatur.</p>
  </div>

  <h2 class="section-tab service-tab service-tab--floor">FLOOR SERVICES</h2>
  <div class="service-copy service-copy--floor">
    <p>Lorem ipsum dolor sit amet, consectetur adipiscing elit, sed do eiusmod tempor incididunt ut labore et dolore magna aliqua. Ut enim ad minim veniam, quis nostrud exercitation ullamco laboris nisi ut aliquip ex ea commodo consequat. Duis aute irure dolor in reprehenderit in voluptate velit esse cillum dolore eu fugiat nulla pariatur.</p>
    <p>Excepteur sint occaecat cupidatat non proident, sunt in culpa qui officia deserunt mollit anim id est laborum.</p>
  </div>

  <div class="photo photo--green" role="img" aria-label="Cleaning caddy with sprays, brushes and sponges held in a yellow-gloved hand" style="left:28px;top:237px;width:198px;height:198px;background:radial-gradient(circle at 55% 55%,#a8e06a 0,#d9d2c6 35%,#b9b1a6 65%,#4b6e7a)"></div>
  <div class="photo photo--green" role="img" aria-label="Blue-gloved hands disinfecting elevator buttons" style="left:40px;top:195px;width:98px;height:98px;background:radial-gradient(circle at 45% 55%,#2f7fd6 0,#8a98a6 55%,#5a6470)"></div>
  <div class="photo photo--green" role="img" aria-label="Flat mop cleaning a blue office floor" style="left:216px;top:293px;width:146px;height:146px;background:radial-gradient(circle at 50% 65%,#e9eef2 0,#9fb6c8 45%,#3f6f99)"></div>
  <div class="photo photo--green" role="img" aria-label="Worker in protective suit disinfecting an office with desks and laptops" style="left:471px;top:196px;width:146px;height:146px;background:radial-gradient(circle at 50% 55%,#f0f2f4 0,#c6ccd3 50%,#5b6068)"></div>

  <p class="abs call-now">CALL NOW FOR A</p>
  <div class="abs estimate">FREE ESTIMATE</div>
  <div class="abs phone-big"><svg viewBox="0 0 12 12"><circle cx="6" cy="6" r="5.2" fill="none" stroke="var(--green)" stroke-width="1"/><path d="M4,3.2 L5.2,4.8 L4.8,5.6 C5.3,6.6 5.8,7 6.4,7.3 L7.1,6.8 L8.6,8 L7.8,8.8 C5.7,8.5 3.6,6.3 3.3,4.1 Z" fill="var(--green)"/></svg>757-555-0142</div>
  <p class="abs web-line web-line--inside">www.brightmoptidewater.com</p>
</section>

</body>
</html>
```